Brell Harbor Company Business Cards

Front and Back Business Card - logo and text setup - cool design. I need workable photoshop or illustrator files so I can setup each employee card with design that is created
Updates

Hi everyone, thank you for the great entries. Please no more white and blue cards - there are so many already - black and silver only now please. thanks!

Target Market(s)

Construction Industry - Facility Managers

Industry/Entity Type

Construction

Contact Information for Business Card

I really like contemporary simplistic looks - clean neat....not opposed to seeing some black backrounds

Requirements
Must have
• Logo/website address with design on front only - www.brellharbor-example.com (logo attached)
• Back:
• Name/Title/Company Address/Phone/email address
Nice to have
• Cool design
Should not have
• Nothing gimmicky like Fire or Water - since we are a Fire Protection company - it has all been done

```html
<!DOCTYPE html>
<html lang="en">
<head>
<meta charset="utf-8">
<title>Brell Harbor Company Business Cards</title>
<link href="https://fonts.googleapis.com/css2?family=Lato:wght@400;700;900&display=swap" rel="stylesheet">
<style>
  :root {
    --page-bg: #c9c9c9;
    --card-dark: #232323;
    --card-light: #f3f4f2;
    --navy: #1f3b73;
    --orange: #ee4b2f;
    --grey-text: #8a8a8a;
    --shadow: 0 6px 14px rgba(0,0,0,0.35);
  }
  * { margin: 0; padding: 0; box-sizing: border-box; }
  html, body {
    width: 1200px; height: 1200px; overflow: hidden;
    background: var(--page-bg);
    font-family: "Lato", sans-serif;
  }
  .card {
    position: absolute;
    left: 250px;
    width: 708px;
    height: 404px;
    box-shadow: var(--shadow);
  }
  .card-front { top: 144px; background: var(--card-dark); }
  .card-back { top: 582px; background: var(--card-light); }

  .front-wordmark {
    position: absolute; left: 0; right: 0; top: 160px;
    text-align: center;
    font-size: 76px; font-weight: 900; line-height: 1;
    color: var(--orange);
    letter-spacing: -1px;
  }
  .front-website {
    position: absolute; left: 0; right: 0; top: 345px;
    text-align: center;
    font-size: 19px; color: var(--orange);
  }

  .back-wordmark {
    position: absolute; right: 41px; top: 52px;
    display: flex; align-items: center; gap: 12px;
    font-size: 50px; font-weight: 900; line-height: 1;
    color: var(--navy);
    letter-spacing: -0.5px;
  }
  .back-wordmark .mark-square {
    width: 18px; height: 18px; background: var(--orange);
  }
  .person-name {
    position: absolute; left: 38px; top: 220px;
    font-size: 21px; font-weight: 700; color: var(--navy);
  }
  .person-name .surname { color: var(--orange); }
  .person-title {
    position: absolute; left: 38px; top: 248px;
    font-size: 15px; color: var(--grey-text);
  }
  .title-rule {
    position: absolute; left: 113px; right: 41px; top: 261px;
    height: 1.5px; background: var(--orange);
  }
  .contact-list {
    position: absolute; left: 38px; top: 285px;
    list-style: none;
  }
  .contact-list li {
    display: flex; align-items: center; gap: 9px;
    height: 21.3px;
    font-size: 15.5px; color: var(--grey-text);
  }
  .contact-list svg { width: 12px; height: 12px; fill: var(--orange); flex: none; }
  .office-address {
    position: absolute; right: 41px; top: 328px;
    text-align: right;
    font-size: 15.5px; line-height: 20.5px; color: var(--grey-text);
  }
</style>
</head>
<body>
  <section class="card card-front">
    <div class="front-wordmark">Brell Harbor</div>
    <div class="front-website">www.brellharbor-example.com</div>
  </section>

  <section class="card card-back">
    <div class="back-wordmark"><span class="mark-square"></span>Brell Harbor</div>

    <div class="person-name">Dana <span class="surname">Whitlow</span></div>
    <div class="person-title">Director</div>
    <div class="title-rule"></div>

    <ul class="contact-list">
      <li>
        <svg viewBox="0 0 12 12"><path d="M2.5 0.5 L4.5 0.5 L5.3 3.3 L3.9 4.4 C4.6 6 6 7.4 7.6 8.1 L8.7 6.7 L11.5 7.5 L11.5 9.5 C11.5 10.8 10.6 11.5 9.5 11.5 C4.5 11 1 7.5 0.5 2.5 C0.5 1.4 1.2 0.5 2.5 0.5 Z"/></svg>
        (555) 014-2290
      </li>
      <li>
        <svg viewBox="0 0 12 12"><rect x="3" y="0.5" width="6" height="3"/><rect x="0.5" y="4" width="11" height="5" rx="1"/><rect x="3" y="7.5" width="6" height="4" fill="#f3f4f2" stroke="#ee4b2f" stroke-width="1"/></svg>
        (555) 014-2291
      </li>
      <li>
        <svg viewBox="0 0 12 12"><path d="M0.5 2 H11.5 V10 H0.5 Z M1.5 3 L6 6.5 L10.5 3" stroke="#f3f4f2" stroke-width="0.9"/></svg>
        info@brellharbor-example.com
      </li>
      <li>
        <svg viewBox="0 0 12 12"><circle cx="6" cy="6" r="5.3" fill="none" stroke="#ee4b2f" stroke-width="1"/><ellipse cx="6" cy="6" rx="2.3" ry="5.3" fill="none" stroke="#ee4b2f" stroke-width="0.9"/><path d="M0.7 6 H11.3 M1.5 3.3 H10.5 M1.5 8.7 H10.5" stroke="#ee4b2f" stroke-width="0.9"/></svg>
        www.brellharbor-example.com
      </li>
    </ul>

    <address class="office-address" style="font-style: normal;">
      48 Quarry Lane<br>
      Millbrook Falls, NY 10000
    </address>
  </section>
</body>
</html>
```